Re-design of an existing website

We are needing a redesign of http://www.corvane-pharmacy.com/. Same colour scheme and content. The design needs to be done using Zurb Foundation 5 with all SCSS included and setup accordingly.

Placeholder images may be used for now as photo's are in progress. Must be responsive and work on all device types.
Updates

PLEASE NOTE: The project manager is currently on holidays until the 6th of September, hopefully we will have a decision closer to this date but it may be a few days after.

Industry/Entity Type

Medical

Coding

Coded - Design and coding required

Number of Pages Required

3 page

Font styles to use
Sans Serif

Requirements
Must have
• Zurb Foundation 5

```html
<!DOCTYPE html>
<html lang="en">
<head>
<meta charset="utf-8">
<title>The Corvane Pharmacy</title>
<link rel="stylesheet" href="https://fonts.googleapis.com/css2?family=Open+Sans:wght@400;600;700;800&display=swap">
<style>
:root{
  --navy:#1b2f7d;
  --navy-dark:#0f1d5c;
  --navy-deep:#0a1548;
  --accent:#2f8ed8;
  --text:#444;
  --muted:#888;
  --line:#e2e2e2;
  --white:#fff;
}
*{box-sizing:border-box;margin:0;padding:0}
html,body{width:758px;height:1200px;overflow:hidden}
body{font-family:"Open Sans",Arial,sans-serif;color:var(--text);background:var(--white);position:relative;font-size:8px}
.wrap{position:absolute;left:30px;right:30px}
/* top */
.utility{top:6px;display:flex;justify-content:flex-end;gap:14px;font-size:7px;color:var(--muted)}
.brand{top:28px;display:flex;align-items:center;gap:8px}
.brand-mark{width:26px;height:26px;background:var(--navy);border-radius:50%}
.brand-name{font-size:17px;font-weight:700;color:var(--navy);line-height:1}
.brand-tag{font-size:6.5px;color:var(--accent);margin-top:3px;font-style:italic}
.header-tools{position:absolute;right:30px;top:40px;display:flex;align-items:center;gap:6px}
.phone{font-size:8px;color:var(--navy);font-weight:700;margin-right:4px}
.social{width:14px;height:14px;border-radius:50%;background:var(--accent)}
.social.alt{background:#d9453a}
.search{width:80px;height:16px;border:1px solid #ccc;border-radius:2px;font-size:6.5px;color:#aaa;padding:3px 5px;margin-left:6px}
/* nav */
.mainnav{position:absolute;top:98px;left:0;right:0;height:24px;background:var(--navy);display:flex;padding-left:30px}
.mainnav a{color:var(--white);font-size:7.5px;font-weight:600;text-decoration:none;padding:0 11px;line-height:24px}
.mainnav a.active{background:var(--accent)}
/* hero */
.hero{position:absolute;top:122px;left:0;right:0;height:318px;background:linear-gradient(120deg,#c9b7a6 0%,#e8d8c6 40%,#f1e6da 60%,#bfa995 100%)}
.hero-copy{position:absolute;top:110px;left:0;right:0;text-align:center;color:var(--white)}
.hero-copy h1{font-size:22px;font-weight:800;letter-spacing:.5px}
.hero-copy p{font-size:8px;width:300px;margin:6px auto 0;line-height:1.4}
.btn{display:inline-block;border:1.5px solid var(--white);color:var(--white);font-size:7px;font-weight:700;padding:6px 14px;margin-top:12px}
.hero-arrow{position:absolute;top:140px;width:20px;height:30px}
.dots{position:absolute;bottom:12px;left:0;right:0;display:flex;justify-content:center;gap:5px}
.dots span{width:6px;height:6px;border-radius:50%;border:1px solid var(--white)}
.dots span.on{background:var(--white)}
/* tiles */
.tiles{top:456px;display:grid;grid-template-columns:repeat(4,1fr);gap:8px}
.tile-photo{height:120px}
.tile-label{text-align:center;font-size:7.5px;font-weight:700;color:var(--navy);margin-top:14px;letter-spacing:.3px}
.rule{top:622px;height:1px;background:var(--line)}
/* content */
.section-title{font-size:10px;font-weight:800;color:var(--navy);text-transform:uppercase;padding-bottom:6px;border-bottom:2px solid var(--accent);display:inline-block}
.celebrate{top:640px;width:330px}
.celebrate-photo{height:150px;margin-top:12px;background:linear-gradient(180deg,#9fc8e6,#e3d9b4 70%,#c9b57f)}
.celebrate p{font-size:7px;line-height:1.6;margin-top:10px;color:#666}
.btn-outline{display:inline-block;border:1px solid var(--navy);color:var(--navy);font-size:6.5px;font-weight:700;padding:5px 10px;margin-top:12px}
.news{top:640px;left:395px;right:30px}
.news-head{display:flex;justify-content:space-between;align-items:flex-start}
.news-list{list-style:none;margin-top:12px}
.news-list li{padding:9px 0 9px 10px;border-bottom:1px solid var(--line);position:relative}
.news-list li::before{content:"";position:absolute;left:0;top:13px;border:3px solid transparent;border-left-color:var(--navy)}
.news-list b{font-size:7px;font-weight:600;color:#333;display:block}
.news-list span{font-size:6px;color:var(--muted)}
/* footer */
.site-footer{position:absolute;top:1000px;left:0;right:0;height:172px;background:var(--navy-dark);color:#d6dcf0}
.footer-cols{position:absolute;top:18px;left:30px;right:30px;display:grid;grid-template-columns:170px 170px 150px 1fr;gap:14px;font-size:6.5px;line-height:1.55}
.footer-cols h4{color:var(--white);font-size:7.5px;margin-bottom:6px}
.footer-cols strong{color:var(--white);display:block;margin-top:6px}
.footer-cols ul{list-style:none}
.badges{display:flex;flex-direction:column;align-items:flex-end;gap:10px}
.badge{width:40px;height:40px;background:var(--white);border-radius:4px}
.badge.wide{width:64px;height:28px}
.copyright{position:absolute;top:1172px;left:0;right:0;height:28px;background:var(--navy-deep);color:#aab3d6;font-size:6px;padding:10px 30px}
</style>
</head>
<body>
<nav class="wrap utility"><span>Directions</span><span>Employment</span><span>News and Notices</span><span>Contact</span></nav>

<header>
  <div class="wrap brand" style="right:auto">
    <span class="brand-mark"></span>
    <div><div class="brand-name">The Corvane Pharmacy</div><div class="brand-tag">"Specialist Service for Special Needs"</div></div>
  </div>
  <div class="header-tools">
    <span class="phone">(03) 5550 1842</span>
    <span class="social"></span><span class="social alt"></span><span class="social"></span><span class="social alt"></span>
    <div class="search">Search</div>
  </div>
</header>

<nav class="mainnav">
  <a class="active">Home</a><a>Community Pharmacy</a><a>CPAP</a><a>NDIS</a><a>Oncology Services</a><a>Home Nursing</a><a>Nutrition</a><a>Compounding</a><a>Surgical Supply</a>
</nav>

<section class="hero" role="img" aria-label="Photo of a mother holding her smiling baby">
  <svg class="hero-arrow" style="left:20px" viewBox="0 0 20 30"><path d="M14 4 L5 15 L14 26" fill="none" stroke="#fff" stroke-width="3"/></svg>
  <svg class="hero-arrow" style="right:20px" viewBox="0 0 20 30"><path d="M6 4 L15 15 L6 26" fill="none" stroke="#fff" stroke-width="3"/></svg>
  <div class="hero-copy">
    <h1>MOTHER AND BABY</h1>
    <p>We understand what a wonderful, exciting and frightening time a new parenthood can be and we are here to offer our support.</p>
    <span class="btn">READ MORE</span>
  </div>
  <div class="dots"><span></span><span></span><span class="on"></span><span></span><span></span></div>
</section>

<section class="wrap tiles">
  <div><div class="tile-photo" role="img" aria-label="Photo of a nurse with an oncology patient" style="background:linear-gradient(135deg,#b8cde0,#e9eef3)"></div><div class="tile-label">ONCOLOGY SERVICES</div></div>
  <div><div class="tile-photo" role="img" aria-label="Photo of a person sleeping" style="background:linear-gradient(135deg,#d8cfc4,#f3efea)"></div><div class="tile-label">SLEEP APNOEA</div></div>
  <div><div class="tile-photo" role="img" aria-label="Photo of pharmacists compounding medicine" style="background:linear-gradient(135deg,#9fb7cf,#e6edf3)"></div><div class="tile-label">PHARMACEUTICAL COMPOUNDING</div></div>
  <div><div class="tile-photo" role="img" aria-label="Photo of a home nurse visiting a patient" style="background:linear-gradient(135deg,#7fa5cc,#dfe9f2)"></div><div class="tile-label">HOME NURSING</div></div>
</section>

<div class="wrap rule"></div>

<section class="wrap celebrate" style="right:auto">
  <h2 class="section-title">Celebrating 38 years of service</h2>
  <div class="celebrate-photo" role="img" aria-label="Photo of a family jumping on a beach"></div>
  <p>Since March 1977 The Corvane Pharmacy has been offering friendly service, professional advice and the products to you and your family. We offer all of the things that you would expect from a regular Pharmacy as well as specialised services. We offer all of the things that you would expect from a regular Pharmacy as well as many more.</p>
  <span class="btn-outline">READ MORE</span>
</section>

<section class="wrap news">
  <div class="news-head">
    <h2 class="section-title">Health News</h2>
    <svg width="22" height="10" viewBox="0 0 22 10"><path d="M5 1 L1 5 L5 9 M17 1 L21 5 L17 9" fill="none" stroke="#1b2f7d" stroke-width="1.5"/></svg>
  </div>
  <ul class="news-list">
    <li><b>Half of Australians have chronic disease - Daily Health Wire</b><span>03 March/2015 12:15PM</span></li>
    <li><b>'Astounding' results for new cancer drug - Daily Health Wire</b><span>03 March/2015 10:42AM</span></li>
    <li><b>Hangovers cost Aussies economy $3bn - Daily Health Wire</b><span>02 March/2015 4:30PM</span></li>
    <li><b>Can diet affect mental health? - Daily Health Wire</b><span>02 March/2015 9:05AM</span></li>
  </ul>
</section>

<footer class="site-footer">
  <div class="footer-cols">
    <div>
      <h4>Opening Hours and Contacts</h4>
      <div>We are open every day of the year.</div>
      <strong>Monday to Friday</strong>7:00am to 8:30pm
      <strong>Saturday</strong>8:00am to 5:00pm
      <strong>Sunday and Public Holidays</strong>9:00am to 1:00pm
    </div>
    <div>
      <h4>Contact Us</h4>
      <div>Level 2 Harbour Medical Building<br>The Corvane Hospital<br>18 Alder Street<br>Southbank VIC 3006</div>
      <strong>Phone</strong>(03) 5550 1842
      <strong>Email</strong>hello@corvanepharmacy.com.au
    </div>
    <div>
      <h4>MENU</h4>
      <ul><li>Home</li><li>Employment</li><li>Community Pharmacy</li><li>CPAP</li><li>NDIS</li><li>Oncology Services</li><li>Home Nursing</li><li>Nutrition</li><li>Compounding</li><li>Surgical Supply</li></ul>
    </div>
    <div class="badges"><span class="badge"></span><span class="badge wide"></span></div>
  </div>
</footer>
<div class="copyright">Copyright &copy; 2015 All Rights Reserved</div>
</body>
</html>
```